prestige web design for KELVA Finance

Hi Guys,

Looking to team up with a creative designer for another of our websites for KELVA finance.
if looking for our similar website www.brimlendco.com.au is one of our other companies. ideally working in our logo being black and white.

Please see attachments for our logo and a description
HOME
VEHICLE
EQUIPMENT
WHO WE ARE
CONTACT US

open to ideas on layout .

touch base if you have any questions.

Target Market(s)

Prestige cars and equipment -trucks earthmoving

Industry/Entity Type

finance

Coding

Coded - Design and coding required

Number of Pages Required

5+ page

Font styles to use
Sans Serif

Colors

Designer to choose colors to be used in the design.

```html
<!DOCTYPE html>
<html lang="en">
<head>
<meta charset="utf-8">
<title>KELVA Finance</title>
<link href="https://fonts.googleapis.com/css2?family=Bebas+Neue&family=Josefin+Sans:wght@400;600;700&display=swap" rel="stylesheet">
<style>
:root{
  --ink:#000;
  --paper:#fff;
  --panel:#1e1e1e;
  --muted:#3a3a3a;
  --line:#8a8a8a;
  --head:"Bebas Neue",sans-serif;
  --body:"Josefin Sans",sans-serif;
}
*{box-sizing:border-box;margin:0;padding:0}
html,body{width:1200px;height:4431px;overflow:hidden;background:var(--paper);color:var(--ink);font-family:var(--body)}
.abs{position:absolute}
.site{position:relative;width:1200px;height:4431px}
.brand{font-family:var(--body);font-weight:700;letter-spacing:1px;white-space:nowrap}
.h2{font-family:var(--head);font-size:42px;line-height:1;letter-spacing:.5px;font-weight:400}
.copy{font-size:13px;line-height:22px}
.btn{display:flex;align-items:center;justify-content:center;font-size:12.5px;border-radius:4px;white-space:nowrap}
.btn-light{background:var(--paper);color:var(--ink)}
.btn-dark{background:var(--ink);color:var(--paper)}
.photo{position:absolute}
/* header */
.topbar{top:0;left:0;width:1200px;height:107px;background:var(--paper)}
.nav{top:45px;left:502px;display:flex;gap:34px;font-size:13px}
.nav .active{border-bottom:2px solid var(--ink);padding-bottom:5px;font-weight:600}
/* dark sections */
.dark{background:var(--ink);color:var(--paper)}
.backdrop{background:var(--panel)}
/* form */
.field{position:absolute;border:1px solid var(--line);border-radius:4px;font-size:12.5px;color:#555;padding:12px 10px}
.ticks li{list-style:none;display:flex;gap:10px;font-size:13px;line-height:22px;margin-bottom:0}
.ticks svg{flex:none;margin-top:3px}
.foot h4{font-family:var(--body);font-weight:700;font-size:16px;letter-spacing:.5px;margin-bottom:26px}
.foot-list li{list-style:none;font-size:12.5px;line-height:27px}
.social{width:34px;height:34px;border:2px solid var(--ink);border-radius:50%}
.social.fill{background:var(--ink)}
</style>
</head>
<body>
<div class="site">

  <!-- Header -->
  <header class="abs topbar">
    <div class="abs brand" style="left:76px;top:30px;font-size:38px">KELVA Finance</div>
    <nav class="abs nav">
      <span class="active">Home</span><span>Vehicle</span><span>Equipment</span><span>Who We Are</span><span>Contact</span>
    </nav>
    <div class="abs btn btn-dark" style="left:978px;top:33px;width:160px;height:41px;gap:12px">
      Free Estimate
      <svg width="34" height="10" viewBox="0 0 34 10"><path d="M0 5H32M27 1l5 4-5 4" stroke="#fff" stroke-width="1.5" fill="none"/></svg>
    </div>
  </header>

  <!-- Hero -->
  <section class="abs" style="left:0;top:107px;width:1200px;height:728px">
    <div class="photo" role="img" aria-label="Two business people shaking hands across a table with a couple seated, in a bright office" style="inset:0;background:linear-gradient(120deg,#3b342e 0%,#8c7d6d 40%,#d9d3cc 70%,#a89c8e 100%)"></div>
    <svg class="abs" style="left:0;top:0" width="1200" height="728" viewBox="0 0 1200 728">
      <polygon points="0,728 244,701 1200,564 1200,728" fill="#fff"/>
      <polygon points="244,701 1200,564 1200,594 244,724" fill="#1e1e1e"/>
      <polygon points="868,642 1200,597 1200,712" fill="#000"/>
      <g stroke="#fff" stroke-width="2"><line x1="42" y1="390" x2="82" y2="390"/><line x1="42" y1="397" x2="82" y2="397"/><line x1="42" y1="404" x2="72" y2="404"/></g>
      <text x="90" y="402" fill="#fff" font-family="Josefin Sans" font-size="13">02</text>
      <g stroke="#1e1e1e" stroke-width="2" fill="none">
        <circle cx="600" cy="626" r="9"/>
        <line x1="600" y1="635" x2="600" y2="708"/>
        <path d="M585 694l15 15 15-15"/>
      </g>
    </svg>
    <div class="abs" style="left:400px;top:335px;width:424px;text-align:center;color:#fff">
      <div style="font-family:var(--head);font-size:42px;line-height:1">FOR YOUR EVERY NEED</div>
      <p class="copy" style="font-size:14px;margin-top:6px">Lorem Ipsum is simply dummy text of the<br>industry has been the industry's.</p>
    </div>
  </section>

  <!-- About -->
  <section class="abs" style="left:0;top:835px;width:1200px;height:597px">
    <div class="photo" role="img" aria-label="Hand holding a pen over a financial document" style="left:76px;top:126px;width:259px;height:316px;background:linear-gradient(160deg,#e7e9ec,#8d96a3 60%,#2f3540)"></div>
    <div class="photo" role="img" aria-label="Hands counting banknotes beside stacks of coins" style="left:358px;top:174px;width:257px;height:316px;background:linear-gradient(160deg,#3b4250,#8d8f92 50%,#c6a86a)"></div>
    <div class="abs" style="left:358px;top:126px;width:24px;height:24px;border:1.5px solid #555"></div>
    <div class="abs" style="left:308px;top:465px;width:26px;height:26px;background:var(--ink)"></div>
    <div class="abs" style="left:664px;top:115px;width:470px">
      <h2 class="h2">MAKERS OF POSSIBLE</h2>
      <div style="width:34px;height:2px;background:var(--ink);margin:16px 0 20px"></div>
      <p class="copy">KELVA Finance has nearly 20 years industry experience, so we certainly understand personal and business lending. We are committed to providing individuals and businesses with tailored financial services that enable them to reach and then exceed their financial goals. We have a vast list of lenders to suit along with an online team ready to help you, so we're easily accessible and here when you need us. Our friendly team of experienced and approachable staff that will listen, understand your situation and lend responsibly.<br>KELVA Finance - Makers of Possible.</p>
      <h2 class="h2" style="margin-top:40px">WHY CHOOSE US?</h2>
      <p class="copy" style="margin-top:14px">Well, because we're here to help you! We care about outcomes AND helping you achieve a stress and enjoyable lending experience.</p>
    </div>
  </section>

  <!-- Vehicle -->
  <section class="abs dark" style="left:0;top:1432px;width:1200px;height:583px">
    <div class="abs" style="left:74px;top:108px;width:500px">
      <h2 class="h2">VEHICLE LOAN</h2>
      <p class="copy" style="margin-top:20px">While you focus on getting the right car, we will focus on getting you the right finance.</p>
      <div class="btn btn-light" style="width:158px;height:41px;margin-top:21px">Free Estimate</div>
      <p class="copy" style="margin-top:38px">Whether you're interested in purchasing a used or new car for yourself or a fleet of vehicles through your business, KELVA's team are well equipped to help you find the car finance that's right for you.</p>
      <div class="btn btn-light" style="width:232px;height:39px;margin-top:30px">Finance Repayment Calculator</div>
    </div>
    <div class="abs backdrop" style="left:878px;top:74px;width:267px;height:426px"></div>
    <div class="photo" role="img" aria-label="Smiling woman at the wheel of a car while a salesman leans in" style="left:626px;top:96px;width:496px;height:377px;background:linear-gradient(135deg,#c9d2db,#5f7f95 45%,#2d4a60)"></div>
  </section>

  <!-- Equipment -->
  <section class="abs" style="left:0;top:2015px;width:1200px;height:718px">
    <div class="photo" role="img" aria-label="Hands holding a burlap money bag marked with a dollar sign" style="left:76px;top:110px;width:498px;height:503px;background:radial-gradient(circle at 50% 45%,#b49a78,#7a6650 55%,#3d352d)"></div>
    <div class="abs" style="left:622px;top:110px;width:516px">
      <h2 class="h2">EQUIPMENT</h2>
      <div style="width:34px;height:2px;background:var(--ink);margin:12px 0 8px"></div>
      <p class="copy">At KELVA, we help businesses of all sizes to secure funding in the form of a business loan for asset purchases from either a bank or private lender.<br>Our dedicated Equipment Finance specialists have extensive industry experience across the agricultural, construction and earthmoving sectors. We'll work with you to understand the specific needs that face your business to keep your equipment up to date.</p>
      <div style="display:flex;gap:11px;margin-top:24px">
        <div class="btn btn-dark" style="width:156px;height:40px">Free Estimate</div>
        <div class="btn btn-dark" style="width:238px;height:40px">Finance Repayment Calculator</div>
      </div>
      <ul class="ticks" style="margin-top:24px">
        <li><svg width="18" height="16" viewBox="0 0 18 16"><circle cx="7" cy="9" r="6" fill="none" stroke="#000" stroke-width="1.5"/><path d="M4 8l3 3 9-10" fill="none" stroke="#000" stroke-width="1.8"/></svg><span>Transport &amp; Logistics: Trucks, Vans, Trailers, Ships, Forklifts, Conveyors, Conveyance Robots etc.</span></li>
        <li><svg width="18" height="16" viewBox="0 0 18 16"><circle cx="7" cy="9" r="6" fill="none" stroke="#000" stroke-width="1.5"/><path d="M4 8l3 3 9-10" fill="none" stroke="#000" stroke-width="1.8"/></svg><span>Construction, Earthmoving, Forestry and Farming: Scaffolding Tower, Digger, Shovel Loggers, Harvesters etc.</span></li>
        <li><svg width="18" height="16" viewBox="0 0 18 16"><circle cx="7" cy="9" r="6" fill="none" stroke="#000" stroke-width="1.5"/><path d="M4 8l3 3 9-10" fill="none" stroke="#000" stroke-width="1.8"/></svg><span>Healthcare: Dental Machinery, Medical Imaging Machines, Veterinary Equipment etc.</span></li>
        <li><svg width="18" height="16" viewBox="0 0 18 16"><circle cx="7" cy="9" r="6" fill="none" stroke="#000" stroke-width="1.5"/><path d="M4 8l3 3 9-10" fill="none" stroke="#000" stroke-width="1.8"/></svg><span>Automotive: Cars, Utes, Motorbikes etc.</span></li>
        <li><svg width="18" height="16" viewBox="0 0 18 16"><circle cx="7" cy="9" r="6" fill="none" stroke="#000" stroke-width="1.5"/><path d="M4 8l3 3 9-10" fill="none" stroke="#000" stroke-width="1.8"/></svg><span>Technology: Computers, Laptops, Printers/Copiers, Servers, Upgrading to New System Software, etc.</span></li>
        <li><svg width="18" height="16" viewBox="0 0 18 16"><circle cx="7" cy="9" r="6" fill="none" stroke="#000" stroke-width="1.5"/><path d="M4 8l3 3 9-10" fill="none" stroke="#000" stroke-width="1.8"/></svg><span>Manufacturing: Industrial Machinery, Textile Machinery, Cosmetics Machinery, Cable Making Machinery etc.</span></li>
      </ul>
    </div>
  </section>

  <!-- Who we are -->
  <section class="abs dark" style="left:0;top:2733px;width:1200px;height:583px">
    <div class="abs" style="left:76px;top:90px;width:500px">
      <h2 class="h2">WHO WE ARE</h2>
      <p class="copy" style="margin-top:26px">The goal of KELVA Finance is to build on the track record of the KELVA business and to create a new benchmark in the Australia's Asset Finance industry, providing good old fashioned localised service that delivers the assets you want when you need them and structured to recognise asset useful life while being sensitive to cashflow.</p>
      <p class="copy" style="margin-top:22px">Providing second to none asset finance support to business owners and individuals alike.</p>
      <p class="copy" style="margin-top:22px">A healthy appetite exists to help our customers with finance for a broad range of motor vehicles (from cars to heavy commercial vehicles), mobile and fixed plant, and business equipment...</p>
      <p class="copy" style="margin-top:22px">for more detail you can contact us today.</p>
    </div>
    <div class="abs backdrop" style="left:878px;top:76px;width:267px;height:426px"></div>
    <div class="photo" role="img" aria-label="Hands counting a fan of banknotes over a desk with a calculator" style="left:633px;top:96px;width:488px;height:382px;background:linear-gradient(140deg,#2b3a4f,#6e7a86 50%,#c9c4b6)"></div>
  </section>

  <!-- Contact -->
  <section class="abs" style="left:0;top:3316px;width:1200px;height:646px">
    <h2 class="h2" style="position:absolute;top:68px;width:1200px;text-align:center">CONTACT US</h2>
    <p class="copy" style="position:absolute;top:128px;width:1200px;text-align:center">To find out how to get <b>KELVA</b> Finance working for<br>you helping with your funding needs.</p>
    <div class="field" style="left:229px;top:198px;width:240px;height:37px">Name*</div>
    <div class="field" style="left:481px;top:198px;width:239px;height:37px">Last Name</div>
    <div class="field" style="left:734px;top:198px;width:237px;height:37px">Phone*</div>
    <div class="field" style="left:229px;top:249px;width:240px;height:38px">Regional Location*</div>
    <div class="field" style="left:481px;top:249px;width:239px;height:38px">Email Address*</div>
    <div class="field" style="left:734px;top:249px;width:237px;height:38px">Subject*</div>
    <div class="field" style="left:229px;top:299px;width:742px;height:133px">Message*</div>
    <div class="abs btn btn-dark" style="left:528px;top:452px;width:158px;height:38px">Send</div>
    <div class="abs" style="left:373px;top:548px;display:flex;align-items:center;gap:8px;font-family:var(--head);font-size:24px">
      <svg width="32" height="32" viewBox="0 0 32 32"><rect width="32" height="32" rx="5" fill="#000"/><path d="M11 8c1 0 3 4 3 5s-2 2-2 3 3 5 5 5 2-2 3-2 5 2 5 3-2 3-4 3C14 25 7 18 7 12c0-2 2-4 4-4z" fill="#fff"/></svg>
      13 48 27 ( 13 KELVA)
    </div>
    <div class="abs" style="left:615px;top:548px;display:flex;align-items:center;gap:8px;font-family:var(--head);font-size:24px">
      <svg width="32" height="32" viewBox="0 0 32 32"><rect width="32" height="32" rx="5" fill="#000"/><rect x="7" y="10" width="18" height="13" fill="#fff"/><path d="M7 10l9 7 9-7" fill="none" stroke="#000" stroke-width="1.5"/></svg>
      INFO@KELVAFINANCE.COM
    </div>
  </section>

  <!-- Footer -->
  <footer class="abs dark foot" style="left:0;top:3962px;width:1200px;height:401px">
    <div class="abs brand" style="left:76px;top:172px;font-size:40px">KELVA Finance</div>
    <div class="abs" style="left:426px;top:112px">
      <h4>QUICK LINKS</h4>
      <ul class="foot-list">
        <li>&gt;&nbsp;&nbsp;<b>Home</b></li><li>&gt;&nbsp;&nbsp;Vehicle</li><li>&gt;&nbsp;&nbsp;Equipment</li><li>&gt;&nbsp;&nbsp;Who We Are</li><li>&gt;&nbsp;&nbsp;Contact</li>
      </ul>
    </div>
    <div class="abs" style="left:603px;top:112px">
      <h4>CONTACT DETAIL</h4>
      <ul class="foot-list">
        <li><svg width="12" height="12" viewBox="0 0 12 12"><path d="M3 0c1 0 2 3 2 3.5S4 5 4 5.5 6 8.5 7 8.5 8 7.5 8.5 7.5 12 8.5 12 9s-1 3-3 3C4 12 0 8 0 3c0-2 2-3 3-3z" fill="#fff"/></svg>&nbsp;&nbsp;000 111 222 333</li>
        <li style="margin-top:17px"><svg width="12" height="10" viewBox="0 0 12 10"><rect width="12" height="10" fill="#fff"/><path d="M0 0l6 5 6-5" fill="none" stroke="#000"/></svg>&nbsp;&nbsp;info@kelvafinance.com</li>
        <li style="margin-top:17px;line-height:22px"><svg width="10" height="13" viewBox="0 0 10 13"><path d="M5 0a5 5 0 0 1 5 5c0 3-5 8-5 8S0 8 0 5a5 5 0 0 1 5-5z" fill="#fff"/><circle cx="5" cy="5" r="2" fill="#000"/></svg>&nbsp;&nbsp;482 Larkspur Rd<br>&nbsp;&nbsp;&nbsp;&nbsp;&nbsp;#210, Dunmore, QA 40217</li>
      </ul>
    </div>
    <div class="abs" style="left:878px;top:112px;width:246px">
      <h4>NEWSLETTER</h4>
      <p style="font-size:12.5px">Lorem Ipsum is simply dummy printing</p>
      <div style="margin-top:12px;height:39px;border:1px solid #fff;border-radius:4px;font-size:12px;font-style:italic;padding:12px 10px">Email Address</div>
      <div class="btn btn-light" style="margin-top:10px;height:39px">SUBSCRIBE</div>
    </div>
  </footer>

  <!-- Bottom bar -->
  <div class="abs" style="left:0;top:4363px;width:1200px;height:68px">
    <p class="abs" style="left:76px;top:28px;font-size:12px">Copyright © 2022 <b>KELVA</b> | <b>Finance</b>. All Rights Reserved.</p>
    <div class="abs" style="left:951px;top:14px;display:flex;gap:13px">
      <span class="social fill"></span><span class="social"></span><span class="social"></span><span class="social"></span>
    </div>
  </div>

</div>
</body>
</html>
```